Copperleaf Haven Website

Here is the link for all the details, images and information you may need about our website:

https://www.filevaultora.net/s/8kq2mz7rt4wp/NIGEL%20HAMMOND.rar?dl=0

Here is a reference on our competitor: http://www.wanderquill.com.au/ and we want as good as this one.

Number of Pages Required

1 page

```html
<!DOCTYPE html>
<html lang="en">
<head>
<meta charset="utf-8">
<title>Copperleaf Haven</title>
<link href="https://fonts.googleapis.com/css2?family=Roboto:wght@300;400;500;700&display=swap" rel="stylesheet">
<style>
:root{
  --brown:#6d5b4f;
  --brown-dark:#574639;
  --green:#1f8a35;
  --green-text:#1d7a2e;
  --orange:#f26d1f;
  --blue:#0b8fd6;
  --blue-dark:#0672b3;
  --panel:#efefef;
  --text:#555;
  --heading:#4a4038;
  --footer:#333;
}
*{box-sizing:border-box;margin:0;padding:0}
html,body{width:803px;height:1200px;overflow:hidden;background:#fff}
body{position:relative;font-family:'Roboto',sans-serif;color:var(--text);font-size:8px;font-weight:300}
.abs{position:absolute}
.header{left:0;top:0;width:803px;height:62px;background:linear-gradient(90deg,var(--brown-dark),var(--brown) 30%,var(--brown));}
.brand{left:50px;top:20px;display:flex;align-items:center;gap:6px;color:#fff;font-weight:700;font-size:12px}
.brand-mark{width:14px;height:14px;border-radius:50%;background:#3fa24a}
.enquiry{left:624px;top:15px;color:#fff;font-size:10px;font-weight:400}
.enquiry svg{vertical-align:-2px;margin-right:4px}
.enquiry .phone{display:block;color:var(--orange);font-size:19px;margin-left:22px;margin-top:1px}
.nav{left:0;top:62px;width:803px;height:36px;background:var(--green)}
.nav ul{list-style:none;display:flex;position:absolute;left:50px;top:6px}
.nav li{color:#fff;font-size:8px;font-weight:500;height:23px;line-height:23px;padding:0 9px;margin-right:6px}
.nav li.active{background:var(--orange);border-radius:3px;padding:0 18px}
.photo{border-radius:3px}
.slider{left:50px;top:101px;width:523px;height:228px;background:linear-gradient(160deg,#3d5a2a,#6f8f4a 45%,#9aa48e 70%,#4c5a3a)}
.slider h1{left:20px;top:56px;color:#fff;font-size:23px;font-weight:700;position:absolute}
.slider p{left:21px;top:86px;width:280px;color:#fff;font-size:13px;font-weight:400;line-height:17px;position:absolute}
.btn-orange{background:var(--orange);color:#fff;font-weight:500;border-radius:4px;text-align:center}
.slider .btn-orange{position:absolute;left:21px;top:146px;width:87px;height:24px;line-height:24px;font-size:9px}
.dots{position:absolute;left:20px;top:203px;display:flex;gap:4px}
.dots i{width:8px;height:8px;border-radius:50%;background:#fff}
.dots i:first-child{background:var(--blue)}
.panel{background:var(--panel);border-radius:3px}
.panel-head{height:28px;line-height:28px;padding-left:10px;color:#fff;font-size:13px;font-weight:400;background:linear-gradient(180deg,var(--blue),var(--blue-dark));border-radius:3px 3px 0 0}
.booking{left:582px;top:101px;width:171px;height:228px}
.field{margin:0 10px 6px;height:19px;background:#fff;border:1px solid #ddd;border-radius:3px;font-size:7.5px;line-height:17px;padding-left:9px;position:relative;color:#777}
.booking form{padding-top:11px}
.field svg{position:absolute;right:6px;top:4px}
.booking .btn-orange{position:absolute;right:10px;top:193px;width:93px;height:24px;line-height:24px;font-size:8px}
h2.section{font-size:18px;font-weight:400;color:var(--heading)}
h2.section b{color:var(--green-text);font-weight:400}
.body-text{font-size:8px;line-height:15.5px}
.btn-blue{background:var(--blue);color:#fff;font-size:8.5px;font-weight:400;text-align:center;border-radius:3px;height:25px;line-height:25px}
.welcome-img{left:351px;top:357px;width:222px;height:160px;background:linear-gradient(180deg,#8fb0d6 0%,#d8e0e8 25%,#3e6b2e 45%,#5f6a52 70%,#8a8a85)}
.rule{height:1px;background:#ccc}
.arrows{left:546px;top:553px}
.accom-img{left:50px;top:583px;width:523px;height:133px;background:linear-gradient(90deg,#3a2418,#8a5a32 30%,#d9a15a 55%,#6b4a2c 75%,#2a1c14)}
.orange-title{color:var(--orange);font-size:12px;font-weight:400}
.quick{left:582px;top:357px;width:171px;height:229px}
.ql-item{display:flex;gap:8px;padding:12px 10px 0 10px;height:65px}
.ql-thumb{width:51px;height:43px;flex:none;border-radius:2px}
.ql-item h4{color:var(--green-text);font-size:9px;font-weight:500;margin-bottom:2px}
.ql-item p{font-size:7.5px;line-height:11px}
.weather{left:582px;top:596px;width:171px;height:62px;background:var(--brown);border-radius:3px;color:#fff}
.weather h3{position:absolute;left:56px;top:10px;font-size:12.5px;font-weight:400}
.weather .cur{position:absolute;left:56px;top:28px;font-size:8.5px;font-weight:500}
.weather .temp{position:absolute;left:56px;top:42px;font-size:7.5px;color:var(--orange);font-weight:400}
.weather svg{position:absolute;left:8px;top:12px}
.maps{left:582px;top:666px;width:171px;height:166px}
.maps p{text-align:center;font-size:8px;line-height:11.5px;padding:8px 6px 6px}
.map-area{margin:0 9px;height:93px;background:linear-gradient(135deg,#4c6a3a,#2c4a6a 45%,#1e3d70);border:1px solid #bbb}
.cards{left:50px;top:854px;display:flex;gap:18px}
.card{width:163px;height:236px;background:var(--panel);border-radius:3px;position:relative}
.card-head{height:27px;line-height:27px;background:var(--green);color:#fff;font-size:11.5px;font-weight:400;padding-left:10px;border-radius:3px 3px 0 0}
.card-img{margin:7px 8px 0;height:84px;border:1px solid #ccc}
.card .orange-title{font-size:10px;line-height:14.5px;padding:8px 8px 0}
.card .body-text{font-size:7.8px;line-height:12.5px;padding:4px 8px 0}
.card .btn-blue{position:absolute;left:8px;top:200px;width:79px}
.footer{left:0;top:1107px;width:803px;height:93px;background:var(--footer);color:#ddd;font-size:7.5px;font-weight:400}
.footer .label{font-size:8.5px;color:#fff}
.social{display:flex;gap:4px;margin-top:10px}
.social i{width:20px;height:20px;border-radius:50%}
.payments{display:flex;gap:4px;margin-top:10px}
.payments i{width:29px;height:18px;border-radius:2px;background:#e8e8e8;border:1px solid #fff}
</style>
</head>
<body>

<header class="abs header">
  <div class="abs brand"><span class="brand-mark"></span>Copperleaf Haven</div>
  <div class="abs enquiry">
    <svg width="14" height="11" viewBox="0 0 14 11"><path d="M1 4c0-2 3-3 6-3s6 1 6 3v1h-3V3.5H4V5H1z" fill="#7fb8e6"/><rect x="3" y="5" width="8" height="5" rx="1" fill="#7fb8e6"/></svg>MAKE ENQUIRIES:
    <span class="phone">0482736159</span>
  </div>
</header>

<nav class="abs nav">
  <ul>
    <li class="active">HOME</li><li>ACCOMMODATION</li><li>EXTRA TOURS</li><li>BOOK ONLINE</li><li>MISSION STATEMENT</li><li>TESTIMONIALS</li><li>MULTIMEDIA</li><li>ABOUT US</li><li>CONTACT US</li>
  </ul>
</nav>

<section class="abs slider photo" role="img" aria-label="Rainforest canopy walkway through lush green trees">
  <h1>COPPERLEAF HAVEN</h1>
  <p>Duis aliquam nibh a dui iaculis viverra id a velit. Vivamus egestas risus in magna varius commodo.</p>
  <div class="btn-orange">BOOK ONLINE</div>
  <div class="dots"><i></i><i></i><i></i><i></i></div>
</section>

<aside class="abs booking panel">
  <div class="panel-head">BOOKING ONLINE</div>
  <form>
    <div class="field">Name</div>
    <div class="field">Email Address</div>
    <div class="field">Contact No.</div>
    <div class="field">From 05/28/2015<svg width="12" height="10" viewBox="0 0 12 10"><rect x=".5" y=".5" width="11" height="9" fill="none" stroke="#888"/><path d="M.5 3h11M3 5h6M3 7h6" stroke="#888"/></svg></div>
    <div class="field">To 05/28/2015<svg width="12" height="10" viewBox="0 0 12 10"><rect x=".5" y=".5" width="11" height="9" fill="none" stroke="#888"/><path d="M.5 3h11M3 5h6M3 7h6" stroke="#888"/></svg></div>
    <div class="field">No.of People</div>
  </form>
  <div class="btn-orange">CHECK AVAILBILITY</div>
</aside>

<section class="abs" style="left:50px;top:353px;width:295px">
  <h2 class="section">Welcome to <b>COPPERLEAF HAVEN</b></h2>
  <p class="body-text" style="margin-top:6px">Aliquam molestie, mi et imperdiet euismod, dui purus auctor tellus, et interdum lacus lectus et ante. Sed accumsan sollicitudin sapien, sit amet adipiscing turpis gravida ac. In congue, neque ac lobortis volutpat, libero mauris varius mi, vitae suscipit ipsum ligula vitae risus. Duis aliquam nibh a dui iaculis viverra id a velit. Vivamus egestas risus in magna varius commodo.</p>
  <div class="btn-blue" style="width:79px;margin-top:16px">READ MORE</div>
</section>
<div class="abs welcome-img photo" role="img" aria-label="Hiker with raised arms on river boulders beneath forested hills"></div>

<div class="abs rule" style="left:50px;top:536px;width:523px"></div>

<h2 class="abs section" style="left:50px;top:551px">Accomodation at <b>COPPERLEAF HAVEN</b></h2>
<svg class="abs arrows" width="27" height="14" viewBox="0 0 27 14"><path d="M6 1L1 7l5 6M21 1l5 6-5 6" fill="none" stroke="#444" stroke-width="1.5"/></svg>
<div class="abs accom-img photo" role="img" aria-label="Warm lamp-lit restaurant interior with diners at tables"></div>
<section class="abs" style="left:50px;top:731px;width:523px">
  <h3 class="orange-title">Aenean a nibh eget turpis vehicula tempus turpis in odio blandit..</h3>
  <p class="body-text" style="margin-top:2px">Aliquam molestie, mi et imperdiet euismod, dui purus auctor tellus, et interdum lacus lectus et ante. Sed accumsan sollicitudin sapien, sit amet adipiscing turpis gravida ac. In congue, neque ac lobortis volutpat, libero mauris varius mi, vitae suscipit ipsum ligula vitae risus. Duis aliquam nibh a dui iaculis viverra id a velit. Vivamus egestas risus in magna varius commodo.</p>
  <div class="btn-blue" style="width:79px;margin-top:14px">READ MORE</div>
</section>

<aside class="abs quick panel">
  <div class="panel-head">QUICK LINKS</div>
  <div class="ql-item"><div class="ql-thumb" role="img" aria-label="Boat on a jungle river" style="background:linear-gradient(160deg,#2f4a2a,#6a8a6a)"></div><div><h4>Aliquam molestie.</h4><p>Duis aliquam nibh a dui iaculis viverra id a velit nibh eget turpis..</p></div></div>
  <div class="ql-item"><div class="ql-thumb" role="img" aria-label="Campfire at night" style="background:linear-gradient(160deg,#2a1a10,#b8642a)"></div><div><h4>Aliquam molestie.</h4><p>Duis aliquam nibh a dui iaculis viverra id a velit nibh eget turpis..</p></div></div>
  <div class="ql-item"><div class="ql-thumb" role="img" aria-label="Crocodile in the water" style="background:linear-gradient(160deg,#1a2a30,#6a7a70)"></div><div><h4>Aliquam molestie.</h4><p>Duis aliquam nibh a dui iaculis viverra id a velit nibh eget turpis..</p></div></div>
</aside>

<aside class="abs weather">
  <svg width="42" height="40" viewBox="0 0 42 40"><circle cx="18" cy="18" r="11" fill="#f5b81c"/><path d="M18 2v4M18 30v4M2 18h4M4 7l3 3M4 29l3-3M29 7l-3 3" stroke="#f5b81c" stroke-width="2"/><ellipse cx="28" cy="25" rx="11" ry="6" fill="#9fb4c8"/><path d="M24 33l-1 4M29 33l-1 4M34 33l-1 4" stroke="#3d8fd6" stroke-width="1.5"/></svg>
  <h3>LOCAL WEATHER</h3>
  <div class="cur">Current Weather :</div>
  <div class="temp">Crains: 22.6o C S 11km/h</div>
</aside>

<aside class="abs maps panel">
  <div class="panel-head">TRAIL MAPS</div>
  <p>Enlarge the map below to see our tour destinations and office locations.</p>
  <div class="map-area" role="img" aria-label="Map of the coastline and reef with tour destinations"></div>
</aside>

<div class="abs rule" style="left:50px;top:841px;width:703px"></div>

<section class="abs cards">
  <article class="card"><div class="card-head">HEADING TITLE</div><div class="card-img" role="img" aria-label="Tropical beach with rocks and headland" style="background:linear-gradient(180deg,#8ec0e8,#4a8a50 45%,#6fb6c8 70%,#5a6068)"></div><h3 class="orange-title">Aenean a nibh eget turpis vehicula tempus..</h3><p class="body-text">Aliquam molestie, mi et imperdiet euismod, dui purus auctor tellus, et interdum lacus lectus et ante.</p><div class="btn-blue">READ MORE</div></article>
  <article class="card"><div class="card-head">HEADING TITLE</div><div class="card-img" role="img" aria-label="River cruise entrance with a large crocodile sculpture" style="background:linear-gradient(180deg,#cfd8d0,#8a8a7a 50%,#4a5a40)"></div><h3 class="orange-title">Aenean a nibh eget turpis vehicula tempus..</h3><p class="body-text">Aliquam molestie, mi et imperdiet euismod, dui purus auctor tellus, et interdum lacus lectus et ante.</p><div class="btn-blue">READ MORE</div></article>
  <article class="card"><div class="card-head">HEADING TITLE</div><div class="card-img" role="img" aria-label="Kangaroos grazing on a grassy field" style="background:linear-gradient(180deg,#6a8a4a,#8aa65a 50%,#7a9a4a)"></div><h3 class="orange-title">Aenean a nibh eget turpis vehicula tempus..</h3><p class="body-text">Aliquam molestie, mi et imperdiet euismod, dui purus auctor tellus, et interdum lacus lectus et ante.</p><div class="btn-blue">READ MORE</div></article>
  <article class="card"><div class="card-head">HEADING TITLE</div><div class="card-img" role="img" aria-label="Stream flowing over smooth boulders" style="background:linear-gradient(180deg,#5a5a4a,#b8b4a8 50%,#7a7a70)"></div><h3 class="orange-title">Aenean a nibh eget turpis vehicula tempus..</h3><p class="body-text">Aliquam molestie, mi et imperdiet euismod, dui purus auctor tellus, et interdum lacus lectus et ante.</p><div class="btn-blue">READ MORE</div></article>
</section>

<footer class="abs footer">
  <div class="abs" style="left:50px;top:25px">Copyright © 2015.CompanyName.All Right Reserved</div>
  <div class="abs" style="left:50px;top:52px"><span style="color:#fff;font-weight:500">COPPERLEAF HAVEN</span>: 4127 Fernvale Road, Glasgow, D07 52KT</div>
  <div class="abs" style="left:50px;top:68px">Ph: <span style="color:#fff">0482736159</span>. &nbsp;| &nbsp;ACN# <span style="color:#fff">617358290</span></div>
  <div class="abs" style="left:411px;top:22px"><span class="label">CONNECT US:</span>
    <div class="social"><i style="background:#3b5a9a"></i><i style="background:#2aa9e0"></i><i style="background:#3a3a3a;border:1px solid #666"></i><i style="background:#cb2027"></i><i style="background:#dd4b39"></i><i style="background:#d8281f"></i></div>
  </div>
  <div class="abs" style="left:592px;top:22px"><span class="label">PAYMENT FACILITY</span>
    <div class="payments"><i></i><i></i><i></i><i></i><i></i></div>
  </div>
</footer>

</body>
</html>
```